Quorvel Landing page redesign

We are looking for a landing page redesign before we officially launch. We want to incorporate the information already on the site at www.Quorvel.example landing page but make it more inviting. There needs to be a sign up section along with clearly stating what we do. Having a place for sample profiles and linking to our blog and podcast is option. More information about all we will be doing is at Quorvel is on the landing page and also on the blog.

Target Market(s)

35 years old and up.

Coding

Coded - Design and coding required

Number of Pages Required

1 page

Requirements
Must have
• The top bar and the bottom bar (with the privacy policy, etc)
• Sign in/up section.
• I don't want to give to much here because I want designers to be creative.
Nice to have
• Prefer not to have a landing page that requires a lot of scrolling at all.

```html
<!DOCTYPE html>
<html lang="en">
<head>
<meta charset="utf-8">
<title>Quorvel — Define Yours</title>
<link href="https://fonts.googleapis.com/css2?family=Roboto:ital,wght@0,400;0,500;0,700;1,400&family=Fira+Sans:wght@300;400&family=Caveat:wght@500&display=swap" rel="stylesheet">
<style>
:root{
  --blue:#1e8fe1;
  --blue-dark:#1877c9;
  --ink:#222;
  --muted:#666;
  --band:#eeeff1;
  --panel:#f4f5f7;
  --card:#f3f3f3;
  --white:#fff;
}
*{box-sizing:border-box;margin:0;padding:0}
html,body{width:732px;height:1200px;overflow:hidden;background:var(--white)}
body{position:relative;font-family:"Roboto",Arial,sans-serif;color:var(--ink)}
.abs{position:absolute}

/* hero */
.hero{left:0;top:0;width:732px;height:330px;
  background:linear-gradient(180deg,#6d7683 0%,#9aa3ad 35%,#c7ccd2 60%,#a9b2bc 100%);overflow:hidden}
.hero-photo{position:absolute;inset:0;
  background:radial-gradient(ellipse at 55% 70%,rgba(40,70,140,.55) 0,rgba(40,70,140,0) 30%),
             radial-gradient(ellipse at 20% 30%,rgba(230,233,238,.6) 0,rgba(230,233,238,0) 45%),
             linear-gradient(180deg,rgba(40,45,55,.45),rgba(40,45,55,.15) 40%,rgba(40,45,55,.3))}
.topbar{left:0;top:0;width:732px;height:41px;border-bottom:1px solid rgba(255,255,255,.35)}
.brand{left:40px;top:6px;color:var(--white);font-size:26px;font-weight:400;letter-spacing:.3px}
.nav{top:15px;color:var(--white);font-size:10px;font-weight:500}
.btn-outline,.btn-solid{top:10px;height:20px;border-radius:10px;font-size:8.5px;font-weight:500;
  display:flex;align-items:center;justify-content:center}
.btn-outline{left:614px;width:38px;border:1px solid var(--white);color:var(--white)}
.btn-solid{left:656px;width:48px;background:var(--white);color:var(--ink)}
.tagline{left:0;width:732px;top:88px;text-align:center;color:var(--white)}
.tagline .name{font-size:14px}
.tagline .motto{font-size:9px;margin-left:6px;letter-spacing:.3px}
.headline{left:0;width:732px;top:114px;text-align:center;color:var(--white);
  font-family:"Caveat",cursive;font-size:32px;letter-spacing:2px}
.feature{top:215px;width:140px;text-align:center;color:var(--white)}
.feature .ring{width:56px;height:56px;margin:0 auto;border:2px solid var(--white);border-radius:50%;
  display:flex;align-items:center;justify-content:center}
.feature h3{font-size:11.5px;font-weight:500;margin-top:10px}
.feature p{font-size:8px;margin-top:2px}

/* signup */
.signup{left:0;top:330px;width:732px;height:55px;background:var(--band)}
.signup-label{left:69px;top:17px;font-size:7.5px;line-height:12px;font-weight:500}
.field{top:18px;width:154px;height:20px;background:var(--white);border:1px solid #d8d8d8;
  font-size:7.5px;color:#999;padding:5px 8px}
.subscribe{left:644px;top:18px;width:71px;height:20px;background:var(--blue);color:var(--white);
  font-size:8px;font-weight:500;display:flex;align-items:center;justify-content:center;letter-spacing:.3px}

/* intro */
.intro{left:0;width:732px;top:404px;text-align:center;font-family:"Fira Sans",sans-serif;
  font-weight:300;font-size:16.5px;line-height:20px;color:#333}
.how{left:274px;top:466px;width:184px;height:30px;border:1px solid var(--blue);border-radius:15px;
  color:var(--blue-dark);font-size:8.5px;font-weight:500;display:flex;align-items:center;justify-content:center}
.how .play{position:absolute;left:6px;top:6px;width:18px;height:18px;border-radius:50%;background:var(--blue)}

/* gallery */
.tile{height:64px}
.tile.tall{height:102px}

/* blog */
.section-title{left:0;width:732px;text-align:center;font-size:13.5px;font-weight:700}
.section-title span{color:var(--blue)}
.dotted{left:32px;width:668px;border-top:1px dashed var(--blue)}
.card{top:724px;width:155px;height:217px;background:var(--card)}
.card .thumb{height:116px}
.card h4{font-size:11px;font-weight:500;margin:12px 11px 0}
.card p{font-size:7.5px;line-height:12px;color:var(--muted);margin:5px 11px 0;height:36px}
.card .meta{position:absolute;left:11px;right:11px;bottom:9px;border-top:1px solid #ddd;padding-top:8px;
  font-size:6.5px;color:#555;display:flex;justify-content:space-between;align-items:center}
.meta svg{vertical-align:-1px;margin-right:4px}

/* testimonials */
.voices{left:0;top:958px;width:732px;height:158px;background:var(--panel)}
.quote{top:1020px;width:250px;font-size:7.5px;line-height:12px;font-style:italic;color:#555}
.quote .who{font-style:normal;color:var(--ink);margin-top:5px;font-size:7.5px}
.avatar{top:1019px;width:46px;height:46px;border-radius:50%;background:linear-gradient(#c9b4a2,#8d7566)}
.divider{left:365px;top:1020px;height:48px;border-left:1px dashed #999}
.skyline{left:0;top:1072px;width:732px;height:44px}

/* footer */
.foot-main{top:1147px;font-size:7.5px;font-weight:500}
.foot-rule{left:32px;top:1165px;width:668px;border-top:1px dashed #ccc}
.foot-small{top:1174px;font-size:6.5px;color:#444}
.foot-brand{left:555px;top:1140px;font-size:12px;color:var(--ink)}
.foot-brand em{font-style:normal;font-size:8px;letter-spacing:2px;color:#555;border-left:1px solid #999;padding-left:7px;margin-left:6px}
</style>
</head>
<body>

<header class="abs hero">
  <div class="hero-photo" role="img" aria-label="Photo of a family sledding down a snowy hill"></div>
  <div class="abs topbar"></div>
  <div class="abs brand">Quorvel</div>
  <div class="abs nav" style="left:320px">BLOG</div>
  <div class="abs nav" style="left:368px">PODCAST</div>
  <div class="abs btn-outline">Log In</div>
  <div class="abs btn-solid">Sign Up</div>
  <div class="abs tagline"><span class="name">Quorvel</span><span class="motto">DEFINE YOURS</span></div>
  <h1 class="abs headline">Enjoy the magic of more time.</h1>

  <div class="abs feature" style="left:39px">
    <div class="ring"><svg width="26" height="26" viewBox="0 0 26 26" fill="none" stroke="#fff" stroke-width="1.6"><rect x="2" y="2" width="22" height="22"/><line x1="2" y1="8" x2="24" y2="8"/><rect x="5" y="11" width="8" height="10"/><line x1="16" y1="12" x2="21" y2="12"/><line x1="16" y1="16" x2="21" y2="16"/><line x1="16" y1="20" x2="21" y2="20"/></svg></div>
    <h3>Create</h3><p>Timelines, Maps, Family Trees</p>
  </div>
  <div class="abs feature" style="left:210px">
    <div class="ring"><svg width="28" height="24" viewBox="0 0 28 24" fill="none" stroke="#fff" stroke-width="2"><rect x="2" y="2" width="24" height="20"/><path d="M14 18l-5-5a3 3 0 0 1 5-3 3 3 0 0 1 5 3z" fill="#fff"/></svg></div>
    <h3>Memorialize</h3><p>Loved Ones</p>
  </div>
  <div class="abs feature" style="left:381px">
    <div class="ring"><svg width="28" height="28" viewBox="0 0 28 28" fill="none" stroke="#fff" stroke-width="1.6"><circle cx="14" cy="6" r="3" fill="#fff"/><path d="M10 11h8v8h-8z" fill="#fff"/><path d="M4 18l4 4M24 18l-4 4M14 21v5M4 18v3M4 18h3M24 18v3M24 18h-3"/></svg></div>
    <h3>Share</h3><p>Family Stories, History and more</p>
  </div>
  <div class="abs feature" style="left:551px">
    <div class="ring"><svg width="22" height="28" viewBox="0 0 22 28" fill="#fff"><path d="M5 12V8a6 6 0 0 1 12 0h-3a3 3 0 0 0-6 0v4z"/><rect x="3" y="12" width="16" height="13" rx="2"/><rect x="10" y="16" width="2" height="5" fill="#888"/></svg></div>
    <h3>Control</h3><p>Your Privacy</p>
  </div>
</header>

<section class="abs signup">
  <svg class="abs" style="left:31px;top:16px" width="24" height="22" viewBox="0 0 24 22" fill="#2b8fe0"><circle cx="6" cy="5" r="3.5"/><circle cx="18" cy="5" r="3.5"/><circle cx="12" cy="9" r="4"/><path d="M0 16a6 6 0 0 1 12 0v2H0zM12 16a6 6 0 0 1 12 0v2H12z"/><path d="M5 20a7 7 0 0 1 14 0v2H5z"/></svg>
  <div class="abs signup-label">Create a New<br>Account</div>
  <div class="abs field" style="left:146px">Full Name *</div>
  <div class="abs field" style="left:312px">Your Email *</div>
  <div class="abs field" style="left:478px">Password *</div>
  <div class="abs subscribe">SUBSCRIBE</div>
</section>

<p class="abs intro">Build multiple Quorvel pages through one account for yourself,<br>your family and to keep loved one's legacies alive.</p>
<div class="abs how"><span class="play"><svg width="18" height="18" viewBox="0 0 18 18"><path d="M7 5.5l5 3.5-5 3.5z" fill="#fff"/></svg></span>How Quorvel Works</div>

<section aria-label="Sample profiles">
  <div class="abs tile" style="left:0;top:505px;width:183px;background:linear-gradient(90deg,#3a3f4a,#6a5c6a,#2d3560)" role="img" aria-label="Photo of people in suits at an event"></div>
  <div class="abs tile" style="left:183px;top:505px;width:183px;background:linear-gradient(90deg,#4b4a4e,#7a6a72,#5c5a4e)" role="img" aria-label="Photo of a woman with a bird of prey"></div>
  <div class="abs tile" style="left:366px;top:505px;width:183px;background:linear-gradient(#7f8a84,#a9ada6)" role="img" aria-label="Photo of runners in a muddy water race"></div>
  <div class="abs tile" style="left:549px;top:505px;width:183px;background:linear-gradient(90deg,#3a3640,#5e4f5a,#2e2b33)" role="img" aria-label="Photo of friends embracing at dusk"></div>
  <div class="abs tile tall" style="left:0;top:569px;width:183px;background:linear-gradient(90deg,#6b3f1e,#c3852b,#c2a03a)" role="img" aria-label="Photo of two fencers in a hall"></div>
  <div class="abs tile tall" style="left:183px;top:569px;width:183px;background:linear-gradient(#4b6a4a,#3d7a6b,#2f5f58)" role="img" aria-label="Photo of paddleboarders on a green bay"></div>
  <div class="abs tile tall" style="left:366px;top:569px;width:183px;background:linear-gradient(90deg,#4a3d35,#8a7565,#5a4a40)" role="img" aria-label="Photo of a man with a birthday cake at dinner"></div>
  <div class="abs tile tall" style="left:549px;top:569px;width:183px;background:linear-gradient(#2e4a7a,#5d7d4a,#3f6a35)" role="img" aria-label="Photo of two boys at a football stadium"></div>
</section>

<h2 class="abs section-title" style="top:677px">Latest <span>Blog &amp; Views</span></h2>
<div class="abs dotted" style="top:701px"></div>

<article class="abs card" style="left:32px">
  <div class="thumb" style="background:linear-gradient(90deg,#d8d2c8,#5a4a3c,#8a5a30)" role="img" aria-label="Photo of a person carrying a leather bag"></div>
  <h4>Standard Post</h4><p>Enim congue blandit. Lorem ipsum dolor sit amet, consectetur adipiscing elit. Quisque...</p>
  <div class="meta"><span><svg width="7" height="7" viewBox="0 0 7 7" fill="#666"><rect y="1" width="7" height="6"/></svg>22 June, 2015</span><span>&#9679; 0</span></div>
</article>
<article class="abs card" style="left:203px">
  <div class="thumb" style="background:linear-gradient(#c9c8c2,#9a9486,#6a5e4e)" role="img" aria-label="Photo of a coffee carafe on a table"></div>
  <h4>Video Post</h4><p>Ultrices posuere cubilia curae curabitur sit amet tortor ut massa commodo. Vestibulum...</p>
  <div class="meta"><span><svg width="7" height="7" viewBox="0 0 7 7" fill="#666"><rect y="1" width="7" height="6"/></svg>22 June, 2015</span><span>&#9679; 0</span></div>
</article>
<article class="abs card" style="left:374px">
  <div class="thumb" style="background:linear-gradient(90deg,#6a4a3a,#a07a62,#5a3e30)" role="img" aria-label="Photo of a chair by a brick wall"></div>
  <h4>Post with Image</h4><p>Enim congue blandit. Lorem ipsum dolor sit amet, consectetur adipiscing elit. Quisque...</p>
  <div class="meta"><span><svg width="7" height="7" viewBox="0 0 7 7" fill="#666"><rect y="1" width="7" height="6"/></svg>22 June, 2015</span><span>&#9679; 0</span></div>
</article>
<article class="abs card" style="left:546px">
  <div class="thumb" style="background:linear-gradient(#cfc6ba,#8a6a4a,#5a4030)" role="img" aria-label="Photo of a leather wallet on a table"></div>
  <h4>Image Post</h4><p>Ultrices posuere cubilia curae curabitur sit amet tortor ut massa commodo. Vestibulum...</p>
  <div class="meta"><span><svg width="7" height="7" viewBox="0 0 7 7" fill="#666"><rect y="1" width="7" height="6"/></svg>22 June, 2015</span><span>&#9679; 3</span></div>
</article>

<section class="abs voices"></section>
<h2 class="abs section-title" style="top:967px">What <span>People Say</span></h2>
<div class="abs dotted" style="top:990px"></div>
<blockquote class="abs quote" style="left:32px;text-align:right">Duis aute irure dolor in reprehenderit in voluptate velit esse cillum dolore eu fugiat nulla pariatur. Excepteur sint occaecat cupidatat non proident, sunt in culpa qui officia deserunt mollit.<div class="who">Milo Harten, Operations Manager</div></blockquote>
<div class="abs avatar" style="left:299px" role="img" aria-label="Portrait of Milo Harten"></div>
<div class="abs divider"></div>
<div class="abs avatar" style="left:386px" role="img" aria-label="Portrait of Nora Vell"></div>
<blockquote class="abs quote" style="left:451px">Provident, similique sunt in culpa qui officia deserunt mollitia animi, id est laborum et dolorum fuga. Et harum quidem rerum facilis est et expedita distinctio. Nam libero tempore, cum soluta nobis.<div class="who">Nora Vell, Creative Designer</div></blockquote>
<div class="abs skyline" role="img" aria-label="Illustration of a city skyline and airport in blue"
  style="background:linear-gradient(90deg,#2b8fe0 0,#2b8fe0 26%,rgba(43,143,224,0) 36%,rgba(43,143,224,0) 60%,#2b8fe0 66%,#2b8fe0 72%,rgba(43,143,224,.35) 82%,rgba(43,143,224,.15) 100%);
  -webkit-mask:linear-gradient(transparent 30%,#000 70%);mask:linear-gradient(transparent 30%,#000 70%)"></div>
<div class="abs" style="left:0;top:1115px;width:732px;border-top:2px solid var(--blue)"></div>

<footer>
  <svg class="abs" style="left:37px;top:1148px" width="8" height="8" viewBox="0 0 8 8" fill="none" stroke="#333" stroke-width="1.4"><circle cx="3.2" cy="3.2" r="2.4"/><line x1="5" y1="5" x2="7.5" y2="7.5"/></svg>
  <div class="abs foot-main" style="left:57px">Help &amp; Contact</div>
  <div class="abs foot-main" style="left:129px">Fees</div>
  <div class="abs foot-main" style="left:162px">Security</div>
  <div class="abs foot-main" style="left:209px">Podcast</div>
  <div class="abs foot-brand">Quorvel<em>DEFINE YOURS</em></div>
  <div class="abs foot-rule"></div>
  <div class="abs foot-small" style="left:37px">About</div>
  <div class="abs foot-small" style="left:68px">Blog</div>
  <div class="abs foot-small" style="left:94px">Jobs</div>
  <div class="abs foot-small" style="left:122px">Data Tracking Policy</div>
  <div class="abs foot-small" style="left:197px">Public Policy</div>
  <div class="abs foot-small" style="left:249px">Sitemap</div>
  <div class="abs foot-small" style="left:287px">Partners</div>
  <div class="abs foot-small" style="left:559px">© 2015–2017</div>
  <div class="abs foot-small" style="left:614px">Terms of Use</div>
  <div class="abs foot-small" style="left:665px">Feedback</div>
</footer>

</body>
</html>
```